Business Card for Coastal Bedrock Consulting

We need a business card for Coastal Bedrock Consulting. The company website address is provided below. The company logo is attached. We provide specialized permafrost services to the mining, transportation, and oil & gas industries. The card should be prepared for:
Randall Whitacre, PhD.
Coastal Bedrock Consulting
PO Box 418539
Moose Hollow, Alaska 99642
Direct: +1-907-555-0143
Email: rwhitacre@bedrockadvisory.example
Website: www.coastalbedrockconsulting.example

```html
<!DOCTYPE html>
<html lang="en">
<head>
<meta charset="utf-8">
<title>Coastal Bedrock Consulting – Business Card</title>
<link href="https://fonts.googleapis.com/css2?family=Quicksand:wght@400;500;600&display=swap" rel="stylesheet">
<style>
  :root {
    --backdrop: #ababab;
    --card-dark: #333333;
    --card-light: #ffffff;
    --ink: #333333;
    --ink-soft: #444444;
    --muted-light: #b9b9b9;
    --logo-on-dark: #a9a9a9;
    --tundra: linear-gradient(160deg, #8a7a5a 0%, #6f6b52 35%, #4d7480 60%, #8a6e4a 100%);
    --ice-core: linear-gradient(135deg, #6e6a64 0%, #9a958d 45%, #7a766f 70%, #d9d9d9 100%);
    --mine-pit: linear-gradient(180deg, #c9ccd2 0%, #7f8088 45%, #5e5d5b 70%, #d4d6db 100%);
  }
  * { box-sizing: border-box; margin: 0; padding: 0; }
  html, body { width: 1200px; height: 1000px; overflow: hidden; }
  body {
    background: var(--backdrop);
    font-family: "Quicksand", sans-serif;
    position: relative;
  }
  .card {
    position: absolute;
    left: 293px;
    width: 615px;
    height: 354px;
    border-radius: 16px;
    overflow: hidden;
  }
  .card--front { top: 132px; background: var(--card-dark); }
  .card--back { top: 530px; background: var(--card-light); }

  .wordmark {
    position: absolute;
    left: 0; right: 0;
    text-align: center;
    font-weight: 600;
    text-transform: uppercase;
    letter-spacing: 3px;
    font-size: 25px;
  }
  .card--front .wordmark { top: 68px; color: var(--logo-on-dark); }
  .card--back .wordmark { top: 56px; color: var(--ink); }

  .photo-strip {
    position: absolute;
    top: 160px;
    left: 0;
    width: 615px;
    height: 138px;
    display: flex;
  }
  .photo { height: 100%; }
  .photo--tundra { width: 201px; background: var(--tundra); }
  .photo--ice { width: 213px; background: var(--ice-core); }
  .photo--mine { width: 201px; background: var(--mine-pit); }

  .website {
    position: absolute;
    top: 318px;
    left: 0; right: 0;
    display: flex;
    justify-content: center;
    align-items: center;
    gap: 5px;
    color: var(--muted-light);
    font-size: 14px;
  }

  .person {
    position: absolute;
    top: 153px;
    left: 0; right: 0;
    text-align: center;
    color: var(--ink);
  }
  .person__name { font-weight: 600; font-size: 17px; line-height: 22px; }
  .person__title { font-weight: 400; font-size: 17px; line-height: 22px; color: var(--ink-soft); }

  .contact {
    position: absolute;
    top: 216px;
    left: 0; right: 0;
    text-align: center;
    color: var(--ink-soft);
    font-size: 17px;
    line-height: 24px;
  }
  .contact__icons {
    display: flex;
    justify-content: center;
    gap: 4px;
    margin-bottom: 4px;
  }
</style>
</head>
<body>

<section class="card card--front">
  <div class="wordmark">Coastal Bedrock Consulting</div>
  <div class="photo-strip">
    <div class="photo photo--tundra" role="img" aria-label="Aerial view of tundra with lakes"></div>
    <div class="photo photo--ice" role="img" aria-label="Close-up of frozen ground layers"></div>
    <div class="photo photo--mine" role="img" aria-label="Snowy mine site with excavator and workers"></div>
  </div>
  <div class="website">
    <svg width="12" height="12" viewBox="0 0 12 12" aria-hidden="true">
      <circle cx="6" cy="6" r="5.3" fill="none" stroke="#b9b9b9" stroke-width="1"/>
      <ellipse cx="6" cy="6" rx="2.3" ry="5.3" fill="none" stroke="#b9b9b9" stroke-width="1"/>
      <line x1="0.7" y1="6" x2="11.3" y2="6" stroke="#b9b9b9" stroke-width="1"/>
    </svg>
    <span>coastalbedrockconsulting.example</span>
  </div>
</section>

<section class="card card--back">
  <div class="wordmark">Coastal Bedrock Consulting</div>
  <div class="person">
    <p class="person__name">Randall Whitacre, PhD.</p>
    <p class="person__title">Principal Consultant</p>
  </div>
  <div class="contact">
    <div class="contact__icons">
      <svg width="22" height="22" viewBox="0 0 22 22" aria-label="Phone">
        <circle cx="11" cy="11" r="11" fill="#333"/>
        <path d="M7.5 6.2c.5-.4 1.1-.3 1.4.2l1 1.6c.2.4.1.9-.2 1.2l-.6.5c.5 1.2 1.5 2.2 2.7 2.7l.5-.6c.3-.3.8-.4 1.2-.2l1.6 1c.5.3.6.9.2 1.4l-.7.8c-.5.5-1.3.7-2 .4-2.5-1-4.5-3-5.5-5.5-.3-.7-.1-1.5.4-2z" fill="#fff"/>
      </svg>
      <svg width="22" height="22" viewBox="0 0 22 22" aria-label="Email">
        <circle cx="11" cy="11" r="11" fill="#333"/>
        <rect x="5.5" y="7" width="11" height="8" rx="1" fill="none" stroke="#fff" stroke-width="1.3"/>
        <path d="M5.8 7.5 11 11.5l5.2-4" fill="none" stroke="#fff" stroke-width="1.3"/>
      </svg>
    </div>
    <p>(907) 555-0143</p>
    <p>rwhitacre@bedrockadvisory.example</p>
  </div>
</section>

</body>
</html>
```